KT Holloway Insurance Group, LLC - Branding Project

We have an existing business card that was designed on Quillmark Press. We recently completed a new logo design with sketch hive and would like to utilize this new logo design into a business card design. Our new logo will be a major emphasis of our branding that is currently under development.

We are an independent insurance agency licensed in Colorado. We specialized in four keys areas. Business Insurance, Risk Management, Employee Benefits and Investments.

We would like the efforts of this design to last for 5 years minimum. Existing business card and new logo design files attached.

Requirements
Must have
• My office is a virtual office. All of our marketing effort drive from the Denver, CO office location. Our mailing address is just for mailing, that's it.
• Please maintain the color scheme of the new logo design.
Nice to have
• Doublesided card, I think? Your the expert if you have other ideas that are better I am excited to see them.

```html
<!DOCTYPE html>
<html lang="en">
<head>
<meta charset="utf-8">
<title>KT Holloway Insurance Group – Business Card</title>
<link href="https://fonts.googleapis.com/css2?family=Didact+Gothic&family=Montserrat:wght@600&display=swap" rel="stylesheet">
<style>
  :root {
    --indigo: #34277f;
    --sky: #1d95d9;
    --paper: #f6f6f6;
    --ink: #3a3a4a;
    --stage: #e4e4ea;
  }
  * { box-sizing: border-box; margin: 0; padding: 0; }
  html, body { width: 1200px; height: 788px; overflow: hidden; }
  body {
    background: var(--stage);
    font-family: "Didact Gothic", "Century Gothic", sans-serif;
    color: var(--ink);
    position: relative;
  }
  .card {
    position: absolute;
    top: 245px;
    width: 520px;
    height: 297px;
    overflow: hidden;
    box-shadow: 0 6px 18px rgba(30, 20, 80, .18);
  }
  .card--front { left: 50px; background: var(--paper); }
  .card--back { left: 630px; background: var(--indigo); }

  /* front */
  .holder { position: absolute; left: 36px; top: 34px; }
  .holder__name {
    font-family: "Montserrat", sans-serif;
    font-weight: 600;
    font-size: 17px;
    letter-spacing: 1.5px;
    color: var(--indigo);
  }
  .holder__title { font-size: 12px; letter-spacing: .5px; margin-top: 2px; }

  .contact { position: absolute; left: 36px; top: 100px; list-style: none; }
  .contact li {
    display: flex; align-items: center; gap: 7px;
    font-size: 11.5px; line-height: 17px; letter-spacing: .3px;
  }
  .contact svg { width: 12px; height: 12px; flex: none; }

  .wordmark {
    position: absolute;
    display: flex; align-items: center; gap: 10px;
    color: var(--indigo);
  }
  .wordmark__dot { border-radius: 50%; background: var(--sky); flex: none; }
  .wordmark__text { line-height: 1; letter-spacing: 1px; }
  .wordmark__text span { display: block; }

  .card--front .wordmark { right: 36px; top: 112px; }
  .card--front .wordmark__dot { width: 34px; height: 34px; }
  .card--front .wordmark__text { font-size: 21px; }
  .card--front .wordmark__text span + span { font-size: 11px; letter-spacing: 3.2px; margin-top: 4px; }

  .address {
    position: absolute; right: 36px; bottom: 30px;
    text-align: right; font-size: 11.5px; line-height: 15px; letter-spacing: .3px;
  }
  .band { position: absolute; left: 0; right: 0; bottom: 0; height: 8px; background: var(--sky); }

  /* back */
  .card--back .wordmark { left: 40px; top: 48px; color: #fff; }
  .card--back .wordmark__dot { width: 40px; height: 40px; }
  .card--back .wordmark__text { font-size: 24px; }
  .card--back .wordmark__text span + span { font-size: 12px; letter-spacing: 3.6px; margin-top: 5px; }
  .web { position: absolute; left: 40px; top: 128px; color: #fff; font-size: 12px; letter-spacing: .4px; }
  .accent {
    position: absolute; right: -40px; bottom: -70px;
    width: 230px; height: 230px; border-radius: 50%;
    background: var(--sky);
  }
</style>
</head>
<body>

<section class="card card--front" aria-label="Business card front">
  <div class="holder">
    <p class="holder__name">KENT HOLLOWAY</p>
    <p class="holder__title">Account Executive</p>
  </div>

  <ul class="contact">
    <li>
      <svg viewBox="0 0 12 12" aria-hidden="true"><rect width="12" height="12" rx="2" fill="var(--sky)"/><path d="M3.5 2.5l1.5 0 .6 1.8-1 .7a5 5 0 0 0 2.4 2.4l.7-1 1.8.6v1.5c0 .4-.3.6-.7.6A6.3 6.3 0 0 1 2.9 3.2c0-.4.2-.7.6-.7z" fill="#fff"/></svg>
      970.555.0141
    </li>
    <li>
      <svg viewBox="0 0 12 12" aria-hidden="true"><rect width="12" height="12" rx="2" fill="var(--sky)"/><rect x="3" y="2.5" width="6" height="7" rx="1" fill="none" stroke="#fff" stroke-width="1"/><rect x="4.5" y="4" width="3" height="2" fill="#fff"/></svg>
      970.555.0142
    </li>
    <li>
      <svg viewBox="0 0 12 12" aria-hidden="true"><rect width="12" height="12" rx="2" fill="var(--sky)"/><rect x="2.5" y="3.5" width="7" height="5" fill="none" stroke="#fff" stroke-width="1"/><path d="M2.5 3.5L6 6.3l3.5-2.8" fill="none" stroke="#fff" stroke-width="1"/></svg>
      kent@kthollowayinsurance.com
    </li>
    <li>
      <svg viewBox="0 0 12 12" aria-hidden="true"><rect width="12" height="12" rx="2" fill="var(--sky)"/><circle cx="6" cy="6" r="3.4" fill="none" stroke="#fff" stroke-width="1"/><path d="M2.6 6h6.8M6 2.6c-1.6 2-1.6 4.8 0 6.8M6 2.6c1.6 2 1.6 4.8 0 6.8" fill="none" stroke="#fff" stroke-width=".8"/></svg>
      www.kthollowayinsurance.com
    </li>
  </ul>

  <div class="wordmark">
    <span class="wordmark__dot" aria-hidden="true"></span>
    <p class="wordmark__text"><span>KT HOLLOWAY</span><span>INSURANCE GROUP</span></p>
  </div>

  <address class="address">
    22 Larimer Commons, 1650 Blake Street<br>
    Suite 300, Denver, CO 80202<br>
    Post Office Box 4417<br>
    Mobile, Alabama 36608
  </address>

  <div class="band"></div>
</section>

<section class="card card--back" aria-label="Business card back">
  <div class="wordmark">
    <span class="wordmark__dot" aria-hidden="true"></span>
    <p class="wordmark__text"><span>KT HOLLOWAY</span><span>INSURANCE GROUP</span></p>
  </div>
  <p class="web">www.kthollowayinsurance.com</p>
  <div class="accent" aria-hidden="true"></div>
</section>

</body>
</html>
```